Kaffeerösterei sucht Etiketten-Design
- schnelle Ausführung - mein Geschmack voll getroffen - unkompliziert und Kunden orientiert bei der Ausführung
Zielgruppe
Kaffeerösterei für die edelsten und teuersten Rohkaffees.
Meine Kunden sind Kaffee Geniesser.
Aufgabenstellung
Transparente Aufkleber für eine Schiefertafel im Format 22.5 cm x 15.5 cm.
Im Hand-Lettering Stil.
5 Schiefertafeln sind gewünscht.
Tafel 1
Kostenlos zur Degustation
Espresso
Café Crème 3.--
Americano 3.--
Filter Kaffee 3.--
Tafel 2
Kaffee & Milch
Cappuccino 4.--
Café Latte 4.--
Flat White 4.--
Latte Macchiato 4.--
Latte Macchiato mit Aroma 5.--
Kaffee & Hafermilch + 1.--
Tafel 3
Crepes
Pikant
- Pizza Crepes 7.--
- Flammkuchen Crepes 7.--
Süss
- Schoggi Crepes 6.--
- Apfelmus & Zimtzucker 6.--
Tafel 4
Kaffee & Schnaps
- Original Entlebucher Schwarzes 7.--
- Espresso Coretto 5.00
- Schwarzes mit Rahmhaube 8.--
Tafel 5
Schokolade & Milch
- heisse Schoggi 5.--
- heisse Schoggi mit Rahmhaube 6.--
- heisse Schoggi mit Espresso 6.--
- Schokolade & Hafermilch +1.--
Als Idee, was mir gefallen könnte:
https://www.bildsammlung.example/pin/104857392018374655/
https://de.grafikhort.example/vektorkunst/4418203-set-kaffeekarte-mit-tassen-kaffeegetranken-im-vintage-stil-stilisierte-zeichnung-mit-kreide-auf-tafel-schriftzug-sample-drinks
https://www.fotolager.example/stockfoto-heisser-kakao-bar-warm-hier-oben-hand-tafel-caf-schild-an-tafel-hintergrund-mit-farbe-kreide-schriftzug-werbung-fur-heisse-d-583021746.html

```html
<!DOCTYPE html>
<html lang="de">
<head>
<meta charset="utf-8">
<title>Kaffee &amp; Milch – Tafel 2</title>
<link href="https://fonts.googleapis.com/css2?family=Amatic+SC:wght@700&family=Kaushan+Script&display=swap" rel="stylesheet">
<style>
  :root {
    --page: #ffffff;
    --slate: #1d1d1b;
    --chalk: #ffffff;
    --cream: #fffadc;
    --price: #fdf0dc;
    --gold: #f9d27a;
    --milk-blue: #a2d9f5;
  }
  * { margin: 0; padding: 0; box-sizing: border-box; }
  html, body {
    width: 1200px; height: 874px; overflow: hidden;
    background: var(--page);
  }
  .board {
    position: absolute;
    left: 63px; top: 60px;
    width: 1076px; height: 741px;
    background: var(--slate);
  }
  .title {
    position: absolute;
    left: 0; right: 0; top: 88px;
    text-align: center;
    font-family: "Kaushan Script", cursive;
    font-size: 104px;
    line-height: 1;
    color: var(--cream);
    white-space: nowrap;
  }
  .title .amp { color: var(--gold); }
  .flourish {
    position: absolute;
    top: 93px; width: 85px; height: 43px;
    background: var(--gold);
    border-radius: 40px;
    opacity: .9;
  }
  .flourish--left { left: 87px; }
  .flourish--right { left: 905px; }
  .jug-illustration {
    position: absolute;
    left: 87px; top: 242px;
    width: 265px; height: 243px;
    border-radius: 50% 50% 40% 40%;
    background: linear-gradient(180deg, var(--slate) 0%, #2c2c2a 55%, var(--milk-blue) 100%);
  }
  .menu {
    position: absolute;
    left: 0; top: 205px;
    width: 1076px;
    list-style: none;
  }
  .menu-item {
    display: flex;
    align-items: baseline;
    height: 81px;
  }
  .menu-item__name {
    width: 820px;
    text-align: right;
    font-family: "Amatic SC", sans-serif;
    font-weight: 700;
    font-size: 74px;
    letter-spacing: 2px;
    line-height: 81px;
    color: var(--chalk);
  }
  .menu-item__note {
    font-size: 40px;
    letter-spacing: 1px;
    margin-left: 14px;
  }
  .menu-item__price {
    margin-left: 22px;
    font-family: "Kaushan Script", cursive;
    font-size: 72px;
    line-height: 81px;
    color: var(--price);
    white-space: nowrap;
  }
</style>
</head>
<body>
  <main class="board">
    <div class="flourish flourish--left" role="img" aria-label="Geschwungenes Zierornament"></div>
    <h1 class="title">Kaffee <span class="amp">&amp;</span> Milch</h1>
    <div class="flourish flourish--right" role="img" aria-label="Geschwungenes Zierornament"></div>

    <div class="jug-illustration" role="img" aria-label="Gezeichnete Milchkanne mit Aufschrift Milk auf einer hellblauen Milchpfütze"></div>

    <ul class="menu">
      <li class="menu-item"><span class="menu-item__name">Cappuccino</span><span class="menu-item__price">4,–</span></li>
      <li class="menu-item"><span class="menu-item__name">Café Latte</span><span class="menu-item__price">4,–</span></li>
      <li class="menu-item"><span class="menu-item__name">Flat White</span><span class="menu-item__price">4,–</span></li>
      <li class="menu-item"><span class="menu-item__name">Latte Macchiato</span><span class="menu-item__price">4,–</span></li>
      <li class="menu-item"><span class="menu-item__name">Latte Macchiato<span class="menu-item__note">mit Aroma</span></span><span class="menu-item__price">5,–</span></li>
      <li class="menu-item"><span class="menu-item__name">Kaffee &amp; Hafermilch</span><span class="menu-item__price">+1,–</span></li>
    </ul>
  </main>
</body>
</html>
```